Business Card Design Project for Heron Lending

Hello there,

We are looking for a business card design for our new Heron Lending car financing company. We are looking for a business card that will include:

- An address
- Telephone number and extension
- Employee Name
- Employee Title
- Our logo and name clearly visible

We are including our logo with this writeup, we are looking to convey friendliness, trus and memorability. Colors and everything else is up to you.

Target Market(s)

18-34 year old males and females

Industry/Entity Type

Business

```html
<!DOCTYPE html>
<html lang="en">
<head>
<meta charset="utf-8">
<title>Heron Lending — Business Card</title>
<link href="https://fonts.googleapis.com/css2?family=Open+Sans:wght@400;700&display=swap" rel="stylesheet">
<style>
  :root {
    --navy: #033a52;
    --paper: #efefed;
    --ink: #231f20;
    --backdrop: #e6e6e6;
    --white: #ffffff;
  }
  * { margin: 0; padding: 0; box-sizing: border-box; }
  html, body { width: 1200px; height: 675px; overflow: hidden; }
  body {
    background: var(--backdrop);
    font-family: "Open Sans", Arial, sans-serif;
    position: relative;
  }
  .card {
    position: absolute;
    top: 189px;
    width: 520px;
    height: 297px;
    overflow: hidden;
  }
  .card--back {
    left: 50px;
    background: var(--navy);
    display: flex;
    align-items: center;
    justify-content: center;
  }
  .card--front {
    left: 630px;
    background: var(--paper);
  }
  .brand-name {
    font-weight: 700;
    letter-spacing: 0.04em;
    display: flex;
    align-items: center;
    gap: 12px;
    white-space: nowrap;
  }
  .card--back .brand-name { color: var(--white); font-size: 40px; }
  .card--back .brand-dot { width: 18px; height: 18px; border-radius: 50%; background: var(--white); }
  .card--front .brand-name {
    position: absolute;
    left: 36px;
    top: 148px;
    color: var(--navy);
    font-size: 28px;
  }
  .card--front .brand-dot { width: 14px; height: 14px; border-radius: 50%; background: var(--navy); }
  .wave { position: absolute; inset: 0; }
  .person {
    position: absolute;
    right: 34px;
    top: 40px;
    text-align: right;
    color: var(--navy);
  }
  .person-name { font-size: 14px; font-weight: 700; line-height: 1.2; }
  .person-title { font-size: 10px; font-weight: 400; }
  .contact {
    position: absolute;
    right: 18px;
    top: 172px;
    text-align: right;
    color: var(--white);
    font-size: 11px;
    line-height: 1.45;
  }
  .contact-line { display: flex; justify-content: flex-end; align-items: flex-start; gap: 6px; }
  .contact-line svg { flex: none; margin-top: 2px; }
</style>
</head>
<body>
  <section class="card card--back">
    <div class="brand-name"><span class="brand-dot"></span>Heron Lending</div>
  </section>

  <section class="card card--front">
    <svg class="wave" viewBox="0 0 520 297" aria-hidden="true">
      <path d="M520,100 C445,108 400,130 368,180 C325,248 215,284 0,292 L0,297 L520,297 Z" fill="var(--navy)"/>
      <path d="M520,100 C445,108 400,130 368,180 C325,248 215,284 0,292" fill="none" stroke="var(--ink)" stroke-width="7" transform="translate(0,-13)"/>
    </svg>

    <div class="person">
      <div class="person-name">Your Long Name</div>
      <div class="person-title">Your Title</div>
    </div>

    <div class="brand-name"><span class="brand-dot"></span>Heron Lending</div>

    <div class="contact">
      <div class="contact-line">
        <span>00.00.00.0000</span>
        <svg width="11" height="11" viewBox="0 0 24 24"><path fill="var(--white)" d="M6.6 10.8a15.1 15.1 0 0 0 6.6 6.6l2.2-2.2a1 1 0 0 1 1-.25 11.4 11.4 0 0 0 3.6.57 1 1 0 0 1 1 1V20a1 1 0 0 1-1 1A17 17 0 0 1 3 4a1 1 0 0 1 1-1h3.5a1 1 0 0 1 1 1c0 1.25.2 2.45.57 3.57a1 1 0 0 1-.25 1z"/></svg>
      </div>
      <div class="contact-line">
        <span>Your Commercial or<br>office address</span>
        <svg width="10" height="12" viewBox="0 0 24 30"><path fill="var(--white)" d="M12 0a10 10 0 0 0-10 10c0 7.5 10 20 10 20s10-12.5 10-20A10 10 0 0 0 12 0zm0 14a4 4 0 1 1 0-8 4 4 0 0 1 0 8z"/></svg>
      </div>
    </div>
  </section>
</body>
</html>
```